vascular clinic webdesign (wordpress+neve theme+ elementor)

Create a nice webdesign for an existing website of a vascular surgery clinic. Vascular surgery is the medical specialty that treats arteries and veins. Content should not change. First landing page we can recreate content if needed, but internal pages should not change content. We currently use Neve theme (https://brovanta.com/themes/kelto/) in a Wordpress CMS, which is highly customizable, we prefer to keep using it, as it is standard in all our sites, and will be often upgraded. We also have Elementor Pro. Please visit current domain: quintela.pro.
Page is in portuguese. But you can do anything in English that I translate later, or you can use original domain content already in portuguese.
Selected design need to be coded in wordpress+neve+elementor

Minimum pages:
First Page/Landing page (https://quintela.pro/)
Contact page (https://quintela.pro/contato/)
Post/Article page
About us (https://quintela.pro/a-clinica/)
Posts Archive (https://quintela.pro/todos-artigos/)
The team (https://quintela.pro/sobre-nos-equipe-de-cirurgia-vascular-endovascular-ecografia-angiologia/)

Designs look the same

Target Market(s)

mostly (70%) woman, 30 to 60 years

Industry/Entity Type

Health

Coding

Coded - Design and coding required

Number of Pages Required

5+ page

Font styles to use
Serif

Requirements
Should not have
• Will not change Wordpress for any other CMS
Prefer not to change theme Neve (https://brovanta.com/themes/kelto/)

```html
<!DOCTYPE html>
<html lang="pt-BR">
<head>
<meta charset="utf-8">
<title>Quintela.pro — propostas de páginas</title>
<link href="https://fonts.googleapis.com/css2?family=Playfair+Display:wght@400;600;700&family=Poppins:wght@400;500;600;700&display=swap" rel="stylesheet">
<style>
:root{
  --board:#ececec;
  --white:#ffffff;
  --ink:#2e2e2e;
  --muted:#777777;
  --red:#7a1d18;
  --red-deep:#5a120f;
  --blue:#1d5b8c;
  --blue-dark:#154a75;
  --blue-soft:#dbe6f0;
  --footer:#262626;
  --gray-band:#f2f2f2;
  --green:#49b35a;
  --serif:'Playfair Display', Georgia, serif;
  --sans:'Poppins', Arial, sans-serif;
}
*{box-sizing:border-box;margin:0;padding:0}
html,body{width:1200px;height:3654px;overflow:hidden}
body{background:var(--board);font-family:var(--sans);color:var(--ink);position:relative}
.abs{position:absolute}
.brand-mark{position:absolute;left:149px;top:372px;font-family:var(--serif);font-size:66px;font-weight:400;color:var(--red-deep);letter-spacing:1px}
.page{position:absolute;width:425px;background:var(--white);overflow:hidden;box-shadow:0 2px 10px rgba(0,0,0,.08)}
.site-header{position:absolute;left:0;top:0;width:100%;height:24px;background:var(--white);z-index:3}
.site-header .logo{position:absolute;left:30px;top:7px;font-family:var(--serif);font-size:8px;color:var(--red-deep)}
.site-header nav{position:absolute;right:24px;top:9px;font-size:4.2px;font-weight:600;display:flex;gap:8px}
.serif{font-family:var(--serif)}
.photo{position:absolute}
.page-hero{position:absolute;left:0;top:24px;width:100%;height:113px;background:linear-gradient(120deg,#4f5e43,#7d8a6c 45%,#9a8f86 70%,#5c6b4d)}
.page-hero h1{position:absolute;left:0;right:0;top:34px;text-align:center;font-family:var(--serif);font-weight:600;font-size:17px;color:var(--white)}
.page-hero .hero-sub{position:absolute;left:0;right:0;top:56px;text-align:center;font-family:var(--serif);font-size:8px;color:var(--white)}
.hero-wave{position:absolute;left:0;bottom:-1px;width:100%;height:40px}
.h2{font-family:var(--serif);font-weight:600;color:var(--ink);text-align:center}
.small{font-size:4.3px;line-height:1.5;color:var(--muted)}
.btn-red{display:inline-block;background:var(--red);color:var(--white);font-size:3.8px;font-weight:700;padding:2px 7px;border-radius:6px}
.btn-white{display:inline-block;background:var(--white);color:var(--ink);font-size:3.8px;font-weight:700;padding:2px 9px;border-radius:6px}
.card{position:absolute;background:var(--white);box-shadow:0 1px 5px rgba(0,0,0,.12);border-radius:3px}
.post-card{position:absolute;width:116px}
.post-card .thumb{height:80px;border-radius:2px}
.post-card h4{font-size:4.6px;font-weight:700;margin-top:8px}
.post-card .meta{font-size:3.2px;color:#999;margin-top:1px}
.post-card p{font-size:3.4px;color:var(--muted);line-height:1.45;margin-top:2px}
.post-card .more{font-size:3.4px;font-weight:700;color:var(--red);margin-top:2px}
.icon-bubble{position:absolute;width:26px;height:26px;border-radius:50%;background:var(--blue-soft)}
.cta-footer{position:absolute;left:0;bottom:0;width:100%;height:290px}
.cta-footer svg{position:absolute;left:0;top:0}
.cta-title{position:absolute;left:0;right:0;top:60px;text-align:center;font-family:var(--serif);font-weight:600;font-size:12px;color:var(--white)}
.cta-btn{position:absolute;left:0;right:0;top:80px;text-align:center}
.foot-logo{position:absolute;left:30px;top:190px;font-family:var(--serif);font-size:9px;color:var(--white)}
.foot-text{position:absolute;left:30px;top:204px;width:82px;font-size:3.3px;line-height:1.5;color:#bbb}
.foot-col{position:absolute;top:188px;font-size:3.3px;line-height:1.75;color:#bbb}
.foot-col b{display:block;font-family:var(--serif);font-size:5px;color:var(--white);font-weight:600}
.socials{position:absolute;left:318px;top:197px;display:flex;gap:4px}
.socials i{width:7px;height:7px;border-radius:50%;background:#555;display:block}
.copyright{position:absolute;left:0;right:0;top:268px;text-align:center;font-size:3.3px;color:#bbb}
.to-top{position:absolute;right:14px;top:266px;width:9px;height:9px;border-radius:50%;background:var(--red)}
.testimonial{position:absolute;left:0;width:100%;text-align:center}
.testimonial .quote{font-family:var(--serif);font-size:24px;color:#cfcfcf;line-height:1}
.testimonial h3{font-family:var(--serif);font-weight:600;font-size:11px;margin-top:-6px}
.testimonial .avatar{width:18px;height:18px;border-radius:50%;background:linear-gradient(#e8ded4,#c9b6a3);margin:6px auto}
.testimonial .said{font-size:4.2px;color:#555;line-height:1.5}
.testimonial .name{font-size:4.2px;font-weight:700;color:var(--red);margin-top:2px}
.dots{display:flex;gap:2px;justify-content:center;margin-top:3px}
.dots i{width:3px;height:3px;border-radius:50%;background:#ccc;display:block}
.dots i.on{background:var(--red)}
.field{background:var(--white);height:9px;border-radius:1px;font-size:3.2px;color:#999;padding:2.5px 3px;margin-bottom:3px}
.member{position:absolute}
.member h3{font-family:var(--serif);font-weight:600;font-size:7.5px;line-height:1.2}
.member p{font-size:3.9px;line-height:1.5;color:#555;margin-top:4px}
.member .mail{color:var(--blue)}
</style>
</head>
<body>

<div class="brand-mark">Quintela.pro</div>

<!-- ============ HOME ============ -->
<section class="page" style="left:149px;top:613px;height:1784px">
  <header class="site-header"><span class="logo">Quintela.pro</span>
    <nav><span>A Clínica</span><span>A Equipe</span><span>Problemas Vasculares</span><span>Soluções</span><span>Contato</span></nav></header>

  <div class="abs" style="left:0;top:24px;width:425px;height:275px;background:linear-gradient(160deg,#f7f1ea,#eef1f4 60%,#e3ebf2)"></div>
  <div class="photo" role="img" aria-label="Pai brincando com o filho ao ar livre" style="left:200px;top:24px;width:225px;height:250px;background:linear-gradient(180deg,#cfe0ee,#e8dccd 60%,#d8c3a8)"></div>
  <h1 class="abs serif" style="left:30px;top:128px;font-size:17px;font-weight:600">Cirurgião Vascular</h1>
  <div class="abs serif" style="left:30px;top:150px;font-size:8px">Cirurgião Vascular em São Paulo</div>
  <div class="abs" style="left:30px;top:163px"><span class="btn-red">AGENDE AGORA!</span></div>
  <div class="abs" style="left:208px;top:231px;width:7px;height:10px;border:0.8px solid #555;border-radius:4px"></div>
  <svg class="abs" style="left:0;top:225px" width="425" height="75" viewBox="0 0 425 75"><path d="M0 75 L0 70 C140 70 250 60 330 30 C370 15 400 8 425 5 L425 75Z" fill="#fff"/><path d="M0 72 C140 72 250 60 330 30 C370 14 400 8 425 4" stroke="#1d5b8c" stroke-width="3" fill="none"/></svg>

  <h2 class="h2 abs" style="left:0;right:0;top:308px;font-size:11.5px;line-height:1.25">Especialista em Cirurgia<br>Vascular e Angiologia</h2>
  <div class="icon-bubble" style="left:72px;top:345px"></div>
  <div class="icon-bubble" style="left:186px;top:345px"></div>
  <div class="icon-bubble" style="left:300px;top:345px"></div>
  <svg class="abs" style="left:80px;top:350px" width="20" height="20" viewBox="0 0 20 20" fill="none" stroke="#7a1d18" stroke-width="1"><path d="M6 2 L8 10 L5 18 M12 2 L12 18"/></svg>
  <svg class="abs" style="left:195px;top:350px" width="20" height="20" viewBox="0 0 20 20" fill="none" stroke="#1d5b8c" stroke-width="1"><path d="M8 2 L8 12 C8 16 14 16 14 12 L12 2"/></svg>
  <svg class="abs" style="left:308px;top:350px" width="20" height="20" viewBox="0 0 20 20" fill="none" stroke="#7a1d18" stroke-width="1"><rect x="3" y="3" width="10" height="14" rx="1"/><path d="M15 8 h3 v8 h-3"/></svg>
  <div class="abs" style="left:40px;top:385px;width:90px;text-align:center;font-size:4.3px;font-weight:700">Tratamento de Varizes<br>com Laser</div>
  <div class="abs" style="left:154px;top:385px;width:90px;text-align:center;font-size:4.3px;font-weight:700">Tratamento de<br>Lipedema</div>
  <div class="abs" style="left:268px;top:385px;width:90px;text-align:center;font-size:4.3px;font-weight:700">Todos convênios por<br>reembolso</div>

  <svg class="abs" style="left:0;top:440px" width="425" height="330" viewBox="0 0 425 330"><path d="M0 100 C120 95 220 60 300 30 C350 12 390 5 425 0 L425 330 L0 330Z" fill="#1d5b8c"/></svg>
  <div class="photo" role="img" aria-label="Homem idoso com dor no joelho" style="left:82px;top:425px;width:135px;height:152px;border-radius:4px;background:linear-gradient(135deg,#e9e2d8,#bfb2a2)"></div>
  <div class="card" style="left:217px;top:455px;width:118px;height:124px;padding:46px 10px 0 10px">
    <div class="serif" style="font-size:8px;font-weight:600">Doenças arteriais</div>
    <div class="small" style="margin-top:3px">A equipe de cirurgia vascular está habituada com cirurgias arteriais endovasculares e tradicionais.</div>
  </div>
  <div class="abs serif" style="left:52px;top:630px;font-size:10.5px;color:#fff;font-weight:600">A clínica.... ou hospital</div>
  <div class="abs" style="left:52px;top:648px;width:180px;font-size:4.2px;line-height:1.5;color:#e3ecf4">O Quintela – Instituto de Medicina Avançada é um hospital dia totalmente equipado para realizar os procedimentos mais modernos de forma minimamente invasiva, com uso de laser, radiofrequência e ecoesclerose. Estamos em um cruzamento conhecido da cidade e oferecemos, além da experiência técnica, todo conforto para sua família.</div>
  <div class="abs" style="left:52px;top:702px"><span class="btn-red">SAIBA MAIS</span></div>
  <div class="abs" style="left:248px;top:604px;width:118px;height:160px;background:var(--red);border-radius:2px;padding:9px 8px">
    <div class="serif" style="color:#fff;font-size:8px;margin-bottom:6px">Agende agora!</div>
    <div class="field">Seu nome (obrigatório)</div>
    <div class="field">Seu e-mail (obrigatório)</div>
    <div class="field" style="height:26px">Sua mensagem</div>
    <span class="btn-white" style="font-size:3.4px;padding:1.5px 5px">ENVIAR</span>
    <div style="background:var(--green);color:#fff;font-size:3.3px;text-align:center;border-radius:5px;padding:2px;margin-top:6px">FALE COM NOSSAS SECRETÁRIAS AGORA</div>
    <div style="color:#fff;font-size:3.3px;text-align:center;margin-top:3px">LIGUE PARA AGORA</div>
  </div>

  <svg class="abs" style="left:200px;top:780px" width="24" height="18" viewBox="0 0 24 18" fill="none" stroke="#1d5b8c" stroke-width="1"><circle cx="7" cy="6" r="3"/><circle cx="17" cy="6" r="3"/><path d="M2 17 C2 11 12 11 12 17 M12 17 C12 11 22 11 22 17"/></svg>
  <h2 class="h2 abs" style="left:0;right:0;top:802px;font-size:11px;line-height:1.2">Almost 40 years taking care of you.<br>4 generations of doctors.</h2>
  <div class="abs" style="left:0;right:0;top:832px;text-align:center;font-size:4px;color:#555;line-height:1.4">Varicose veins and spider veins : laser treatment (CLaCs technique)<br>and more (sclerotherapy)</div>

  <div class="photo" role="img" aria-label="Ilustração de médico examinando uma perna" style="left:48px;top:868px;width:150px;height:112px;background:linear-gradient(135deg,#f4e9ee,#d5e3f0 55%,#b8cde2)"></div>
  <div class="abs serif" style="left:212px;top:900px;width:185px;font-size:9.5px;font-weight:600;line-height:1.2">Cirurgia de Aneurisma, Estenose de Carótida, varizes com laser e outras doenças vasculares</div>
  <div class="abs" style="left:212px;top:940px;font-size:4px;color:#555">Vascular Surgeon in São Paulo, SP</div>

  <div class="abs" style="left:0;top:988px;width:425px;height:150px;background:var(--gray-band)"></div>
  <h2 class="h2 abs" style="left:0;right:0;top:1010px;font-size:11px">Especialidades</h2>
  <div class="card" style="left:55px;top:1035px;width:48px;height:50px"></div>
  <div class="card" style="left:109px;top:1035px;width:48px;height:50px"></div>
  <div class="card" style="left:163px;top:1035px;width:48px;height:50px"></div>
  <div class="card" style="left:217px;top:1035px;width:48px;height:50px"></div>
  <div class="card" style="left:271px;top:1035px;width:48px;height:50px"></div>
  <div class="card" style="left:325px;top:1035px;width:48px;height:50px"></div>
  <div class="abs" style="left:55px;top:1066px;width:318px;display:flex;font-size:3.5px;text-align:center;line-height:1.3">
    <span style="width:48px;margin-right:6px">Cirurgia<br>Arterial</span><span style="width:48px;margin-right:6px">Cirurgia<br>Venosa</span><span style="width:48px;margin-right:6px">Tratamento<br>Linfático</span><span style="width:48px;margin-right:6px">Cirurgia<br>Endovascular</span><span style="width:48px;margin-right:6px">Cirurgia de<br>varizes com Laser</span><span style="width:48px">Lipedema</span></div>
  <svg class="abs" style="left:55px;top:1042px" width="318" height="20" viewBox="0 0 318 20" fill="none" stroke="#1d5b8c" stroke-width="0.9"><path d="M20 3 L24 17 L28 3"/><path d="M74 3 C78 10 70 12 80 17"/><path d="M126 4 L138 16 M138 4 L126 16"/><path d="M184 3 L180 17 M188 3 L184 17"/><path d="M236 4 L246 16 M246 4 L236 16"/><path d="M292 3 C286 10 296 12 290 17"/></svg>

  <h2 class="h2 abs" style="left:0;right:0;top:1168px;font-size:11px">Blog mais recente</h2>
  <article class="post-card" style="left:31px;top:1198px"><div class="thumb" role="img" aria-label="Frutas vermelhas em potes" style="background:linear-gradient(135deg,#f1f1f3,#6b6fb8 55%,#c93b4a)"></div><h4>Probiotics</h4><div class="meta">January 9, 2021 · No Comments</div><p>Os probióticos estão sendo cada vez mais utilizados na medicina. Os probióticos são...</p><div class="more">READ MORE</div></article>
  <article class="post-card" style="left:153px;top:1198px"><div class="thumb" role="img" aria-label="Pés sobre lençol branco" style="background:linear-gradient(135deg,#e9e9e9,#c9b8a8)"></div><h4>What is Godet's sign?</h4><div class="meta">January 9, 2021 · No Comments</div><p>Have you heard of Godet's sign? Although the name is somewhat unknown, the sign is...</p><div class="more">READ MORE</div></article>
  <article class="post-card" style="left:275px;top:1198px"><div class="thumb" role="img" aria-label="Prato de comida mediterrânea" style="background:linear-gradient(135deg,#4d3a2a,#8f6b3f 50%,#5d7d3a)"></div><h4>How to make the Mediterra...</h4><div class="meta">January 9, 2021 · No Comments</div><p>The Mediterranean diet, also known as the Mediterranean diet, is a simple way...</p><div class="more">READ MORE</div></article>

  <div class="testimonial" style="top:1345px"><div class="quote">“</div><h3>Ainda com dúvidas?</h3><div class="small">Veja os testemunhos do nosso serviço. Eles vão tirar suas dúvidas.</div><div class="avatar" role="img" aria-label="Foto da paciente"></div><div class="said">Fiz uma cirurgia plástica para tratar Lipedema no início de dezembro de 2019<br>e desde o primeiro contato foi muito bem atendida</div><div class="name">Marisa</div><div class="dots"><i></i><i class="on"></i><i></i></div></div>

  <div class="cta-footer">
    <svg width="425" height="290" viewBox="0 0 425 290"><defs><linearGradient id="rg1" x1="0" y1="0" x2="1" y2="1"><stop offset="0" stop-color="#8a1f18"/><stop offset="1" stop-color="#4a0e0b"/></linearGradient></defs><path d="M0 40 C120 40 260 30 425 0 L425 180 L0 180Z" fill="url(#rg1)"/><path d="M0 150 C120 120 250 150 330 140 C370 135 400 120 425 115 L425 290 L0 290Z" fill="#262626"/><path d="M0 150 C120 120 250 150 330 140 C370 135 400 120 425 115" stroke="#1d5b8c" stroke-width="3" fill="none"/></svg>
    <div class="cta-title">Sua família saudável.</div>
    <div class="cta-btn"><span class="btn-white">AGENDE UMA CONSULTA</span></div>
    <div class="foot-logo">Quintela.pro</div>
    <div class="foot-text">A história da equipe de cirurgia vascular se mistura à história da cirurgia vascular no Brasil. O nosso legado também é uma história muito legal. Mais de 4 décadas tratando problemas vasculares.</div>
    <div class="foot-col" style="left:178px"><b>Useful Links</b>A Clínica<br>A Equipe<br>Problemas Vasculares<br>Soluções<br>Contato</div>
    <div class="foot-col" style="left:248px"><b>Importantes</b>Mapa e Endereço<br>Sintomas Vasculares<br>Lipedema</div>
    <div class="socials"><i></i><i></i><i></i><i></i><i></i></div>
    <div class="copyright">Copyright © 2020. Sua equipe médica de confiança de Cirurgia Vascular em São Paulo, SP</div>
    <div class="to-top"></div>
  </div>
</section>

<!-- ============ TODOS ARTIGOS ============ -->
<section class="page" style="left:149px;top:2403px;height:763px">
  <header class="site-header"><span class="logo">Quintela.pro</span>
    <nav><span>A Clínica</span><span>A Equipe</span><span>Problemas Vasculares</span><span>Soluções</span><span>Contato</span></nav></header>
  <div class="page-hero" role="img" aria-label="Vista aérea da clínica"><h1>Todos artigos</h1>
    <svg class="hero-wave" viewBox="0 0 425 40" preserveAspectRatio="none"><path d="M0 40 L0 35 C150 35 280 25 425 2 L425 40Z" fill="#fff"/><path d="M0 36 C150 36 280 25 425 3" stroke="#1d5b8c" stroke-width="3" fill="none"/></svg></div>
  <article class="post-card" style="left:31px;top:168px"><div class="thumb" role="img" aria-label="Frutas vermelhas em potes" style="background:linear-gradient(135deg,#f1f1f3,#6b6fb8 55%,#c93b4a)"></div><h4>Probiotics</h4><div class="meta">January 9, 2021 · No Comments</div><p>Os probióticos estão sendo cada vez mais utilizados na medicina...</p><div class="more">READ MORE</div></article>
  <article class="post-card" style="left:153px;top:168px"><div class="thumb" role="img" aria-label="Pés sobre lençol branco" style="background:linear-gradient(135deg,#e9e9e9,#c9b8a8)"></div><h4>What is Godet's sign?</h4><div class="meta">January 9, 2021 · No Comments</div><p>Have you heard of Godet's sign? Although the name is unknown...</p><div class="more">READ MORE</div></article>
  <article class="post-card" style="left:275px;top:168px"><div class="thumb" role="img" aria-label="Prato de comida mediterrânea" style="background:linear-gradient(135deg,#4d3a2a,#8f6b3f 50%,#5d7d3a)"></div><h4>How to make the Mediterra...</h4><div class="meta">January 9, 2021 · No Comments</div><p>The Mediterranean diet is a simple way of eating...</p><div class="more">READ MORE</div></article>
  <article class="post-card" style="left:31px;top:308px"><div class="thumb" role="img" aria-label="Balança e fita métrica" style="background:linear-gradient(135deg,#dfe8ee,#7fa3bf)"></div><h4>Do you need to lose weight to operate on varicose veins?</h4><div class="meta">January 9, 2021 · No Comments</div><p>Você já ouviu falar que precisa perder peso para operar...</p><div class="more">READ MORE</div></article>
  <article class="post-card" style="left:153px;top:308px"><div class="thumb" role="img" aria-label="Pernas subindo escada" style="background:linear-gradient(135deg,#3b3a3a,#b07a5c)"></div><h4>List of signs and symptoms of Lipedema</h4><div class="meta">January 9, 2021 · No Comments</div><p>O Lipedema é a symmetrical increase in fat, usually...</p><div class="more">READ MORE</div></article>
  <article class="post-card" style="left:275px;top:308px"><div class="thumb" role="img" aria-label="Médica examinando perna com varizes" style="background:linear-gradient(135deg,#eef0f2,#d9bfae)"></div><h4>Confira 5 tipos de tratamentos de varizes</h4><div class="meta">January 9, 2021 · No Comments</div><p>As varizes atingem uma parcela considerável da população...</p><div class="more">READ MORE</div></article>
  <div class="abs" style="left:0;right:0;top:453px;display:flex;justify-content:center;gap:5px;font-size:3.6px;align-items:center">
    <span style="color:#999">‹ Prev</span><span style="width:8px;height:8px;border-radius:50%;background:var(--red);color:#fff;text-align:center;line-height:8px">1</span><span>2</span><span>3</span><span>…</span><span>10</span><span class="btn-red" style="font-size:3.4px">Next ›</span></div>
  <div class="cta-footer">
    <svg width="425" height="290" viewBox="0 0 425 290"><defs><linearGradient id="rg2" x1="0" y1="0" x2="1" y2="1"><stop offset="0" stop-color="#8a1f18"/><stop offset="1" stop-color="#4a0e0b"/></linearGradient></defs><path d="M0 40 C120 40 260 30 425 0 L425 180 L0 180Z" fill="url(#rg2)"/><path d="M0 150 C120 120 250 150 330 140 C370 135 400 120 425 115 L425 290 L0 290Z" fill="#262626"/><path d="M0 150 C120 120 250 150 330 140 C370 135 400 120 425 115" stroke="#1d5b8c" stroke-width="3" fill="none"/></svg>
    <div class="cta-title">Sua família saudável.</div>
    <div class="cta-btn"><span class="btn-white">AGENDE UMA CONSULTA</span></div>
    <div class="foot-logo">Quintela.pro</div>
    <div class="foot-text">A história da equipe de cirurgia vascular se mistura à história da cirurgia vascular no Brasil. O nosso legado também é uma história muito legal. Mais de 4 décadas tratando problemas vasculares.</div>
    <div class="foot-col" style="left:178px"><b>Useful Links</b>A Clínica<br>A Equipe<br>Problemas Vasculares<br>Soluções<br>Contato</div>
    <div class="foot-col" style="left:248px"><b>Importantes</b>Mapa e Endereço<br>Sintomas Vasculares<br>Lipedema</div>
    <div class="socials"><i></i><i></i><i></i><i></i><i></i></div>
    <div class="copyright">Copyright © 2020. Sua equipe médica de confiança de Cirurgia Vascular em São Paulo, SP</div>
    <div class="to-top"></div>
  </div>
</section>

<!-- ============ SOBRE NÓS ============ -->
<section class="page" style="left:627px;top:267px;height:964px">
  <header class="site-header"><span class="logo">Quintela.pro</span>
    <nav><span>A Clínica</span><span>A Equipe</span><span>Problemas Vasculares</span><span>Soluções</span><span>Contato</span></nav></header>
  <div class="page-hero" role="img" aria-label="Vista aérea da clínica"><h1>Sobre nós</h1>
    <svg class="hero-wave" viewBox="0 0 425 40" preserveAspectRatio="none"><path d="M0 40 L0 35 C150 35 280 25 425 2 L425 40Z" fill="#fff"/><path d="M0 36 C150 36 280 25 425 3" stroke="#1d5b8c" stroke-width="3" fill="none"/></svg></div>
  <div class="photo" role="img" aria-label="Aquarela da fachada da clínica" style="left:30px;top:158px;width:170px;height:125px;background:linear-gradient(135deg,#f3eeea,#e6a9a1 45%,#dfe7ee)"></div>
  <div class="abs serif" style="left:218px;top:180px;width:180px;font-size:9px;font-weight:600;line-height:1.2">A Clínica de Cirurgia Vascular em São Paulo no Instituto Quintela</div>
  <ul class="abs" style="left:224px;top:206px;font-size:4.1px;line-height:1.6;color:#555;list-style:none">
    <li>• A História da Clínica</li><li>• A Equipe</li><li>• Day hospital</li><li>• Localização da equipe de cirurgia vascular</li><li>• Procedimentos que realizamos</li><li>• Navegue em 360°dentro da clínica de cirurgia vascular</li><li>&nbsp;&nbsp;e do nosso centro cirúrgico</li></ul>
  <div class="abs serif" style="left:30px;top:345px;font-size:9px;font-weight:600">O que você achou deste artigo?</div>
  <div class="abs" style="left:30px;top:359px;font-size:4px;color:#555">Clique nas estrelas</div>
  <div class="abs" style="left:30px;top:365px;font-size:6px;color:#e0a21b;letter-spacing:1px">★★★★★</div>
  <div class="abs" style="left:30px;top:374px;font-size:3.8px;color:#777">Average rating 5 / 5. Number of votes</div>
  <div class="photo" role="img" aria-label="Fachada da clínica" style="left:212px;top:300px;width:213px;height:122px;background:linear-gradient(180deg,#3f5a2e,#b7463a 45%,#d9d4cd 80%,#8a8a8a)"></div>
  <div class="card" style="left:30px;top:445px;width:118px;height:100px;text-align:center;padding:20px 8px 0"><svg width="18" height="16" viewBox="0 0 18 16" fill="none" stroke="#7a1d18" stroke-width="1"><rect x="2" y="3" width="14" height="12"/><path d="M2 7h14M6 1v4M12 1v4"/></svg><div style="font-size:6px;font-weight:700;margin-top:3px">35 anos</div><div class="small" style="font-size:3.5px">Estamos há 35 anos tratando de doenças vasculares. Sim, são mais de 3 décadas de empenho.</div></div>
  <div class="card" style="left:153px;top:440px;width:118px;height:110px;background:var(--blue);text-align:center;padding:22px 8px 0;color:#fff"><svg width="22" height="16" viewBox="0 0 22 16" fill="none" stroke="#fff" stroke-width="1"><circle cx="6" cy="5" r="3"/><circle cx="16" cy="5" r="3"/><path d="M1 15c0-5 10-5 10 0M11 15c0-5 10-5 10 0"/></svg><div style="font-size:6px;font-weight:700;margin-top:3px">4 gerações</div><div style="font-size:3.5px;line-height:1.5;color:#dde8f2">São 4 gerações de cirurgiões na família. Conhecimento que passa por gerações.</div></div>
  <div class="card" style="left:276px;top:445px;width:118px;height:100px;text-align:center;padding:20px 8px 0"><svg width="18" height="16" viewBox="0 0 18 16" fill="none" stroke="#7a1d18" stroke-width="1"><circle cx="4" cy="4" r="2"/><circle cx="14" cy="12" r="2"/><path d="M6 4h8M4 6v4h8"/></svg><div style="font-size:6px;font-weight:700;margin-top:3px">+10.000 procedimentos</div><div class="small" style="font-size:3.5px">Mais de 10mil procedimentos vasculares realizados com segurança.</div></div>
  <div class="testimonial" style="top:560px"><div class="quote">“</div><h3>Ainda com dúvidas?</h3><div class="small">Veja os testemunhos do nosso serviço. Eles vão tirar suas dúvidas.</div><div class="avatar" role="img" aria-label="Foto da paciente"></div><div class="said">Fiz uma cirurgia plástica para tratar Lipedema no início de dezembro de 2019<br>e desde o primeiro contato foi muito bem atendida</div><div class="name">Marisa</div><div class="dots"><i></i><i class="on"></i><i></i></div></div>
  <div class="cta-footer">
    <svg width="425" height="290" viewBox="0 0 425 290"><defs><linearGradient id="rg3" x1="0" y1="0" x2="1" y2="1"><stop offset="0" stop-color="#8a1f18"/><stop offset="1" stop-color="#4a0e0b"/></linearGradient></defs><path d="M0 40 C120 40 260 30 425 0 L425 180 L0 180Z" fill="url(#rg3)"/><path d="M0 150 C120 120 250 150 330 140 C370 135 400 120 425 115 L425 290 L0 290Z" fill="#262626"/><path d="M0 150 C120 120 250 150 330 140 C370 135 400 120 425 115" stroke="#1d5b8c" stroke-width="3" fill="none"/></svg>
    <div class="cta-title">Sua família saudável.</div>
    <div class="cta-btn"><span class="btn-white">AGENDE UMA CONSULTA</span></div>
    <div class="foot-logo">Quintela.pro</div>
    <div class="foot-text">A história da equipe de cirurgia vascular se mistura à história da cirurgia vascular no Brasil. O nosso legado também é uma história muito legal. Mais de 4 décadas tratando problemas vasculares.</div>
    <div class="foot-col" style="left:178px"><b>Useful Links</b>A Clínica<br>A Equipe<br>Problemas Vasculares<br>Soluções<br>Contato</div>
    <div class="foot-col" style="left:248px"><b>Importantes</b>Mapa e Endereço<br>Sintomas Vasculares<br>Lipedema</div>
    <div class="socials"><i></i><i></i><i></i><i></i><i></i></div>
    <div class="copyright">Copyright © 2020. Sua equipe médica de confiança de Cirurgia Vascular em São Paulo, SP</div>
    <div class="to-top"></div>
  </div>
</section>

<!-- ============ THE TEAM ============ -->
<section class="page" style="left:627px;top:1272px;height:1224px">
  <header class="site-header"><span class="logo">Quintela.pro</span>
    <nav><span>A Clínica</span><span>A Equipe</span><span>Problemas Vasculares</span><span>Soluções</span><span>Contato</span></nav></header>
  <div class="page-hero" role="img" aria-label="Vista aérea da clínica"><h1>The team</h1>
    <svg class="hero-wave" viewBox="0 0 425 40" preserveAspectRatio="none"><path d="M0 40 L0 35 C150 35 280 25 425 2 L425 40Z" fill="#fff"/><path d="M0 36 C150 36 280 25 425 3" stroke="#1d5b8c" stroke-width="3" fill="none"/></svg></div>
  <div class="abs serif" style="left:78px;top:160px;width:280px;font-size:9px;font-weight:600;line-height:1.25">Sobre nós: Equipe de Cirurgia Vascular, Endovascular, Ecografia, Angiologia</div>
  <div class="abs" style="left:78px;top:187px;width:280px;font-size:4px;line-height:1.55;color:#555">Este portal não pretende realizar consultas, pareceres ou realizar diagnóstico e tratamento via online. Consultas médicas não devem, e não podem ser realizadas via internet. É vedado ao médico prescrever tratamento ou outros procedimentos sem exame direto do paciente (Art. 114 do código de ética médica). É muito importante que os interessados entrem em contato com o seu médico de confiança. É preciso uma consulta presencial para estabelecer um bom tratamento.<br>Caso queira uma consulta, agende através deste formulário ou pelo telefone (11) 4000-1234.</div>
  <div class="photo" role="img" aria-label="Retrato do Prof. Dr. Henrique Lemos Barreto" style="left:63px;top:266px;width:97px;height:134px;background:linear-gradient(180deg,#d9d9d9,#b8b8b8 50%,#eeeeee)"></div>
  <div class="member" style="left:183px;top:293px;width:175px"><h3>Prof. Dr. Henrique Lemos<br>Barreto</h3><p>Cirurgião Vascular, Endovascular e Ecografia Vascular. Doutor em Medicina pela Universidade Vale Claro. Médico Assistente do Hospital. Professor Assistente da Disciplina de Cirurgia Vascular. Membro titular da Associação Vale Claro de Cirurgia Vascular. CRM 00000.<br><span class="mail">henrique@quintela.pro</span></p></div>
  <div class="member" style="left:65px;top:438px;width:175px"><h3>Prof. Dr. Otávio Barreto</h3><p>Angiologia, Cirurgia Vascular e Endovascular. Assistente estrangeiro em hospital universitário. Mestre em Ciências pela Universidade Vale Claro. Presidente da Academia de Medicina Vale Claro. Professor Titular de Cirurgia Vascular. CRM 00000.<br><span class="mail">otavio@quintela.pro</span></p></div>
  <div class="photo" role="img" aria-label="Retrato do Prof. Dr. Otávio Barreto" style="left:250px;top:407px;width:95px;height:136px;background:linear-gradient(180deg,#f1f1f1,#3a3a3a 70%,#2a2a2a)"></div>
  <div class="photo" role="img" aria-label="Retrato do Prof. Dr. Renato Barreto" style="left:63px;top:546px;width:97px;height:134px;background:linear-gradient(180deg,#eeeeee,#3c3c3c 70%)"></div>
  <div class="member" style="left:183px;top:580px;width:175px"><h3>Prof. Dr. Renato Barreto</h3><p>Neurocirurgião. Médico e Neurocirurgião pela Universidade Vale Claro. Neurocirurgião do Hospital de Assistência. Médico Diarista. CRM 00000.<br><span class="mail">renato@quintela.pro</span></p></div>
  <div class="member" style="left:65px;top:705px;width:175px"><h3>Prof. Dr. Caio Vilela</h3><p>Cirurgia Vascular e Endovascular. Prof. Assistente da disciplina de Cirurgia Vascular. Título de especialista em Angiologia e Cirurgia Vascular. Área de atuação em Angiorradiologia e Cirurgia Endovascular. CRM 00000.<br><span class="mail">consulta@quintela.pro</span></p></div>
  <div class="photo" role="img" aria-label="Retrato do Prof. Dr. Caio Vilela" style="left:250px;top:668px;width:95px;height:133px;background:linear-gradient(180deg,#eef1f4,#c9d3dd 60%,#e9eef3)"></div>
  <div class="photo" role="img" aria-label="Retrato do Dr. Tiago Barreto" style="left:63px;top:805px;width:97px;height:135px;background:linear-gradient(180deg,#d5d5d5,#6a6a6a 60%,#bdbdbd)"></div>
  <div class="member" style="left:183px;top:855px;width:175px"><h3>Dr. Tiago Barreto</h3><p>Cirurgia Plástica. Membro do Colégio Vale Claro de Cirurgia Plástica. Formado pela Faculdade de Medicina Vale Claro. CRM 000000.<br><span class="mail">tiago@quintela.pro</span></p></div>
  <div class="cta-footer">
    <svg width="425" height="290" viewBox="0 0 425 290"><defs><linearGradient id="rg4" x1="0" y1="0" x2="1" y2="1"><stop offset="0" stop-color="#8a1f18"/><stop offset="1" stop-color="#4a0e0b"/></linearGradient></defs><path d="M0 40 C120 40 260 30 425 0 L425 180 L0 180Z" fill="url(#rg4)"/><path d="M0 150 C120 120 250 150 330 140 C370 135 400 120 425 115 L425 290 L0 290Z" fill="#262626"/><path d="M0 150 C120 120 250 150 330 140 C370 135 400 120 425 115" stroke="#1d5b8c" stroke-width="3" fill="none"/></svg>
    <div class="cta-title">Sua família saudável.</div>
    <div class="cta-btn"><span class="btn-white">AGENDE UMA CONSULTA</span></div>
    <div class="foot-logo">Quintela.pro</div>
    <div class="foot-text">A história da equipe de cirurgia vascular se mistura à história da cirurgia vascular no Brasil. O nosso legado também é uma história muito legal. Mais de 4 décadas tratando problemas vasculares.</div>
    <div class="foot-col" style="left:178px"><b>Useful Links</b>A Clínica<br>A Equipe<br>Problemas Vasculares<br>Soluções<br>Contato</div>
    <div class="foot-col" style="left:248px"><b>Importantes</b>Mapa e Endereço<br>Sintomas Vasculares<br>Lipedema</div>
    <div class="socials"><i></i><i></i><i></i><i></i><i></i></div>
    <div class="copyright">Copyright © 2020. Sua equipe médica de confiança de Cirurgia Vascular em São Paulo, SP</div>
    <div class="to-top"></div>
  </div>
</section>

<!-- ============ CONTATO ============ -->
<section class="page" style="left:627px;top:2534px;height:962px">
  <header class="site-header"><span class="logo">Quintela.pro</span>
    <nav><span>A Clínica</span><span>A Equipe</span><span>Problemas Vasculares</span><span>Soluções</span><span style="color:var(--red)">Contato</span></nav></header>
  <div class="page-hero" role="img" aria-label="Vista aérea da clínica"><h1 style="top:26px">Fale conosco</h1><div class="hero-sub" style="top:47px">Cuide da saúde e beleza vascular</div>
    <svg class="hero-wave" viewBox="0 0 425 40" preserveAspectRatio="none"><path d="M0 40 L0 35 C150 35 280 25 425 2 L425 40Z" fill="#fff"/><path d="M0 36 C150 36 280 25 425 3" stroke="#1d5b8c" stroke-width="3" fill="none"/></svg></div>
  <div class="icon-bubble" style="left:70px;top:155px"></div>
  <div class="icon-bubble" style="left:183px;top:155px"></div>
  <div class="icon-bubble" style="left:297px;top:155px"></div>
  <svg class="abs" style="left:80px;top:165px" width="16" height="16" viewBox="0 0 16 16" fill="none" stroke="#1d5b8c" stroke-width="1"><circle cx="8" cy="8" r="6"/><path d="M5 6c1 3 2 4 5 5"/></svg>
  <svg class="abs" style="left:192px;top:166px" width="18" height="13" viewBox="0 0 18 13" fill="none" stroke="#7a1d18" stroke-width="1"><rect x="1" y="1" width="16" height="11"/><path d="M1 1l8 6 8-6"/></svg>
  <svg class="abs" style="left:307px;top:163px" width="14" height="18" viewBox="0 0 14 18" fill="none" stroke="#1d5b8c" stroke-width="1"><path d="M7 17C2 10 1 8 1 6a6 6 0 0112 0c0 2-1 4-6 11z"/><circle cx="7" cy="6" r="2"/></svg>
  <div class="abs" style="left:48px;top:188px;width:75px;text-align:center;font-size:4.8px;font-weight:700">WhatsApp<div style="font-size:3.4px;font-weight:400;color:#777">Entre em contato pelo WhatsApp</div></div>
  <div class="abs" style="left:160px;top:188px;width:75px;text-align:center;font-size:4.8px;font-weight:700">Email<div style="font-size:3.4px;font-weight:400;color:#777">secretaria@quintela.pro</div></div>
  <div class="abs" style="left:272px;top:188px;width:80px;text-align:center;font-size:4.8px;font-weight:700">Endereço<div style="font-size:3.4px;font-weight:400;color:#777">Rua das Acácias, 410, São Paulo, SP</div></div>
  <div class="abs" style="left:0;right:0;top:213px;text-align:center;font-size:3.8px;font-weight:600;color:var(--red)">Fale com nossas secretárias pelo WhatsApp agora</div>
  <div class="abs serif" style="left:30px;top:288px;font-size:9px;font-weight:600">Entre em contato com o doutor!</div>
  <div class="abs" style="left:30px;top:302px;width:180px;font-size:4px;line-height:1.55;color:#555">Este portal não pretende realizar consultas, pareceres ou realizar diagnóstico e tratamento via online. Consultas médicas não devem, e não podem ser realizadas via internet. É vedado ao médico prescrever tratamento sem exame direto do paciente (Art. 114 do código de ética médica). É muito importante que os interessados entrem em contato com o seu médico de confiança. É preciso uma consulta presencial para estabelecer um bom tratamento.<br>Caso queira uma consulta, agende através deste formulário ou pelo telefone (11) 4000-1234.</div>
  <div class="abs" style="left:245px;top:256px;width:132px;height:136px;background:var(--blue);border-radius:3px;padding:10px 8px">
    <div style="display:flex;gap:3px"><div class="field" style="flex:1">Seu nome</div><div class="field" style="flex:1">Seu e-mail</div></div>
    <div style="display:flex;gap:3px"><div class="field" style="flex:1">Telefone</div><div class="field" style="flex:1">Cidade/Estado</div></div>
    <div style="display:flex;gap:3px"><div class="field" style="flex:1">Assunto</div><div class="field" style="flex:1">Data</div></div>
    <div class="field" style="height:34px">Sua mensagem</div>
    <div style="background:var(--red);color:#fff;font-size:3.6px;font-weight:700;text-align:center;padding:2.5px;margin-top:4px">ENVIAR</div>
  </div>
  <div class="photo" role="img" aria-label="Mapa da localização da clínica" style="left:0;top:430px;width:425px;height:170px;background:linear-gradient(135deg,#eef0f2,#e3e6ea 50%,#dfe8e0)"></div>
  <div class="card" style="left:30px;top:447px;width:122px;height:138px;padding:9px 9px">
    <div class="serif" style="font-size:5.5px;font-weight:600">Nosso Endereço completo:</div>
    <div style="font-size:3.5px;color:#555;line-height:1.5">Rua das Acácias, 410, São Paulo, SP. CEP 00000-000. Brasil.</div>
    <div class="serif" style="font-size:5.5px;font-weight:600;margin-top:5px">Telefones:</div>
    <div style="font-size:3.5px;color:#555;line-height:1.6">• Fixo: +55 11 4000-1234<br>• Celular: +55 11 90000-0000<br>• secretaria@quintela.pro<br>• consulta@quintela.pro</div>
    <div class="serif" style="font-size:5.5px;font-weight:600;margin-top:5px">Nossos horários:</div>
    <div style="font-size:3.5px;color:#555;line-height:1.5">Segunda a sexta: 8:00 às 19:00<br>Sábado: 8:00 às 12:00</div>
  </div>
  <div class="abs" style="left:50px;top:615px;width:150px"><div class="serif" style="font-size:7px;font-weight:600">Algumas doenças que tratamos</div><div style="font-size:3.8px;color:#555;line-height:1.6;margin-top:3px">• Lipedema<br>• Varizes, trombose e outras doenças venosas<br>• Doenças arteriais: aneurisma, estenose, aterosclerose<br>• Doenças linfáticas</div></div>
  <div class="abs" style="left:225px;top:615px;width:150px"><div class="serif" style="font-size:7px;font-weight:600">Alguns tratamentos que fazemos</div><div style="font-size:3.8px;color:#555;line-height:1.6;margin-top:3px">• laser para varizes<br>• cirurgia de lipedema</div></div>
  <div class="cta-footer">
    <svg width="425" height="290" viewBox="0 0 425 290"><defs><linearGradient id="rg5" x1="0" y1="0" x2="1" y2="1"><stop offset="0" stop-color="#8a1f18"/><stop offset="1" stop-color="#4a0e0b"/></linearGradient></defs><path d="M0 40 C120 40 260 30 425 0 L425 180 L0 180Z" fill="url(#rg5)"/><path d="M0 150 C120 120 250 150 330 140 C370 135 400 120 425 115 L425 290 L0 290Z" fill="#262626"/><path d="M0 150 C120 120 250 150 330 140 C370 135 400 120 425 115" stroke="#1d5b8c" stroke-width="3" fill="none"/></svg>
    <div class="cta-title">Sua família saudável.</div>
    <div class="cta-btn"><span class="btn-white">AGENDE UMA CONSULTA</span></div>
    <div class="foot-logo">Quintela.pro</div>
    <div class="foot-text">A história da equipe de cirurgia vascular se mistura à história da cirurgia vascular no Brasil. O nosso legado também é uma história muito legal. Mais de 4 décadas tratando problemas vasculares.</div>
    <div class="foot-col" style="left:178px"><b>Useful Links</b>A Clínica<br>A Equipe<br>Problemas Vasculares<br>Soluções<br>Contato</div>
    <div class="foot-col" style="left:248px"><b>Importantes</b>Mapa e Endereço<br>Sintomas Vasculares<br>Lipedema</div>
    <div class="socials"><i></i><i></i><i></i><i></i><i></i></div>
    <div class="copyright">Copyright © 2020. Sua equipe médica de confiança de Cirurgia Vascular em São Paulo, SP</div>
    <div class="to-top"></div>
  </div>
</section>

</body>
</html>
```